Service company standing banner design

We are an existing company that just updated our logo. We are attending some oportunity summits in the near future and want a new crisp clean look on our three banners that will be placed in the back of our small booth. The summits we are attending are designed to give local companies opportunities on a prokect we have been awarded to construct in their area. These banners should communicate who we are with no questions when people see them. One banner shall list our services. One to list our values and one to state our goals. All these while being appealing to the eye and using picture of nature. Attached are copies of what we are to replace. also the new logo and the original background pictures in the existing banners

```html
<!DOCTYPE html>
<html lang="en">
<head>
<meta charset="utf-8">
<title>Norvale Services — Values Banner</title>
<link rel="stylesheet" href="https://fonts.googleapis.com/css2?family=Fjalla+One&display=swap">
<style>
  :root {
    --paper: #ffffff;
    --brand-blue: #1d4fae;
    --scene-top: #cf5f7d;
    --scene-mid: #a64d6e;
    --scene-low: #7a4563;
    --scene-base: #4f3a52;
    --value-text: #ffffff;
  }
  html, body {
    margin: 0;
    padding: 0;
    width: 1200px;
    height: 2400px;
    overflow: hidden;
    background: var(--paper);
  }
  .banner {
    position: relative;
    width: 1200px;
    height: 2400px;
    overflow: hidden;
    font-family: "Fjalla One", "Arial Narrow", sans-serif;
  }
  .nature-scene {
    position: absolute;
    inset: 0;
    background:
      radial-gradient(ellipse 520px 900px at 640px 1500px, rgba(235,170,190,0.35), transparent 70%),
      linear-gradient(180deg, var(--scene-top) 0%, var(--scene-top) 22%, var(--scene-mid) 50%, var(--scene-low) 72%, var(--scene-base) 100%);
  }
  .torn-header {
    position: absolute;
    left: 0;
    top: 0;
    width: 1200px;
    height: 560px;
  }
  .brand {
    position: absolute;
    left: 60px;
    top: 70px;
    display: flex;
    align-items: center;
    gap: 40px;
  }
  .brand-mark {
    width: 220px;
    height: 220px;
    border-radius: 50%;
    background: var(--brand-blue);
  }
  .brand-name {
    margin: 0;
    color: var(--brand-blue);
    font-weight: 400;
    line-height: 1.05;
    font-size: 92px;
  }
  .brand-name span { display: block; }
  .brand-name .brand-sub { font-size: 70px; }
  .values {
    list-style: none;
    margin: 0;
    padding: 0;
  }
  .value {
    position: absolute;
    left: 96px;
    display: flex;
    align-items: center;
    gap: 34px;
    color: var(--value-text);
    font-size: 100px;
    letter-spacing: 0.16em;
    line-height: 1;
  }
  .value-tick { width: 58px; height: 58px; flex: none; margin-top: 24px; }
  .value--integrity { top: 760px; }
  .value--respect { top: 1112px; }
  .value--trust { top: 1464px; }
  .value--transparency { top: 1816px; }
</style>
</head>
<body>
<main class="banner">
  <div class="nature-scene" role="img" aria-label="Misty wet road leading through a pine forest under a rose-tinted overlay"></div>

  <svg class="torn-header" viewBox="0 0 1200 560" aria-hidden="true">
    <path fill="var(--paper)" d="M0 0 H1200 V530 L1175 515 1150 498 1120 470 1095 462 1070 440 1040 430 1010 418 985 395 955 388 930 372 900 360 870 352 850 340 820 345 790 338 760 344 730 336 700 340 670 338 640 344 610 338 580 342 560 352 540 348 510 340 480 346 455 342 430 336 400 344 380 350 360 346 340 336 320 340 300 330 280 320 255 318 230 300 205 292 180 278 150 268 125 262 100 252 70 248 40 240 0 236 Z"/>
  </svg>

  <header class="brand">
    <div class="brand-mark" aria-hidden="true"></div>
    <h1 class="brand-name"><span>Norvale Services</span><span class="brand-sub">Limited Partnership</span></h1>
  </header>

  <ul class="values">
    <li class="value value--integrity">
      <svg class="value-tick" viewBox="0 0 20 20" aria-hidden="true"><path d="M3 11 L8 15 L17 5" fill="none" stroke="var(--value-text)" stroke-width="2.6" stroke-linecap="round" stroke-linejoin="round"/></svg>
      <span>INTEGRITY</span>
    </li>
    <li class="value value--respect">
      <svg class="value-tick" viewBox="0 0 20 20" aria-hidden="true"><path d="M3 11 L8 15 L17 5" fill="none" stroke="var(--value-text)" stroke-width="2.6" stroke-linecap="round" stroke-linejoin="round"/></svg>
      <span>RESPECT</span>
    </li>
    <li class="value value--trust">
      <svg class="value-tick" viewBox="0 0 20 20" aria-hidden="true"><path d="M3 11 L8 15 L17 5" fill="none" stroke="var(--value-text)" stroke-width="2.6" stroke-linecap="round" stroke-linejoin="round"/></svg>
      <span>TRUST</span>
    </li>
    <li class="value value--transparency">
      <svg class="value-tick" viewBox="0 0 20 20" aria-hidden="true"><path d="M3 11 L8 15 L17 5" fill="none" stroke="var(--value-text)" stroke-width="2.6" stroke-linecap="round" stroke-linejoin="round"/></svg>
      <span>TRANSPARENCY</span>
    </li>
  </ul>
</main>
</body>
</html>
```